high-impact, conversion-focused website redesign for the government sector

Objective: To design and develop a high-impact, conversion-focused digital platform that solidifies Harrowgate Lumen Advisors (HLA) as the leading communications and strategy firm for government, defense, and industrial clients. The site must project authority, innovation, and sophisticated precision. See the creative breif for more information

Target Market(s)

Government contractors

Industry/Entity Type

Government, defense, industrials

Coding

Coded - Design and coding required

Number of Pages Required

5+ page

Font styles to use
Other font styles liked:
• See the current website

Requirements
Must have
• See design brief
Nice to have
• See design brief
Should not have
• See design brief

```html
<!DOCTYPE html>
<html lang="en">
<head>
<meta charset="utf-8">
<title>Harrowgate Lumen Advisors — Accelerate Your Mission</title>
<link rel="stylesheet" href="https://fonts.googleapis.com/css2?family=Michroma&family=Poppins:wght@400;500;600&display=swap">
<style>
:root{
  --navy:#0f2c52;
  --navy-deep:#0a2142;
  --blue:#1f93f1;
  --blue-soft:#3aa0f4;
  --orange:#f7941d;
  --green:#7cc242;
  --ink:#141414;
  --muted:#555b66;
  --card:#f1f3f6;
  --white:#ffffff;
  --display:"Michroma",sans-serif;
  --body:"Poppins",sans-serif;
}
*{box-sizing:border-box;margin:0;padding:0}
html,body{width:1200px;height:4750px;overflow:hidden;background:var(--white)}
body{font-family:var(--body);color:var(--ink);position:relative}
.abs{position:absolute}
.display{font-family:var(--display);font-weight:400;text-transform:uppercase;letter-spacing:.5px;line-height:1.25}
.btn{position:absolute;display:flex;align-items:center;padding-left:20px;background:var(--blue);color:var(--white);font-size:12px;font-weight:500}
.btn .dot{position:absolute;right:14px;top:50%;width:10px;height:10px;margin-top:-5px;background:var(--orange)}

/* hero */
.hero{position:absolute;left:0;top:0;width:1200px;height:605px}
.hero-visual{position:absolute;inset:0;background:radial-gradient(ellipse at 70% 30%,#3f8fe0 0%,#1a5fb8 35%,#0c3a82 65%,#082a63 100%)}
.nav a{position:absolute;top:37px;color:var(--white);font-size:12px;text-decoration:none}
.brand{position:absolute;display:flex;align-items:center;gap:8px;color:var(--white);font-family:var(--display);font-size:12px;text-transform:uppercase;white-space:nowrap}
.brand i{display:block;width:14px;height:14px;background:var(--orange)}
.welcome{left:125px;top:204px;color:var(--white);font-size:14px}
.welcome b{font-weight:600}
.hero-mark{left:125px;top:274px;width:64px;height:64px;background:var(--blue-soft)}
.hero-copy{left:227px;top:274px;width:340px;color:var(--white);font-size:10px;line-height:18px}
.hero-title{left:122px;top:382px;color:var(--white);font-size:54px;line-height:66px;white-space:nowrap}
.hero-title .outline{color:transparent;-webkit-text-stroke:1.4px var(--white)}

/* intro */
.intro-visual{left:125px;top:700px;width:437px;height:378px;background:linear-gradient(135deg,#4aa3f0 0%,#1557b0 55%,#0a2c6a 100%)}
.intro-title{left:592px;top:716px;font-size:30px}
.intro-copy{left:592px;top:775px;width:480px;font-size:12.5px;line-height:22.5px;color:#222}
.intro-copy p{margin-bottom:22px}

/* results */
.results-title{left:125px;top:1180px;font-size:30px;line-height:38px}
.results-copy{left:125px;top:1308px;width:420px;font-size:9.5px;line-height:18px;color:#333}
.growth-title{left:125px;top:1401px;font-size:16px;line-height:22px;white-space:nowrap}
.stat{font-family:var(--display);font-size:31px}
.stat-note{font-size:9.5px;line-height:18px;color:#333;width:190px}
.arrow-btn{width:33px;height:33px;background:var(--green);display:flex;align-items:center;justify-content:center;top:1690px}
.quote-card{position:absolute;padding:18px 16px 0 16px;overflow:hidden}
.quote-card .who{display:flex;gap:12px;align-items:flex-start;margin-bottom:12px}
.avatar{width:38px;height:38px;border-radius:50%;background:#c8ced8;flex:none}
.who .name{font-family:var(--display);font-size:14px;text-transform:uppercase;line-height:18px}
.who .role{font-family:var(--display);font-size:10px;text-transform:uppercase;line-height:14px}
.quote-card p{font-size:9px;line-height:18px}
.qmark{position:absolute;font-family:Georgia,serif;font-size:70px;line-height:1;font-weight:700}
.faded{background:#fafbfc;color:#b9bec6}
.faded .avatar{background:#e2e6ec}
.active{background:var(--blue);color:var(--white)}

/* services */
.services-band{left:0;top:1840px;width:1200px;height:288px;background:var(--navy)}
.services-title{left:0;top:1884px;width:1200px;text-align:center;color:var(--white);font-size:30px}
.svc{position:absolute;width:304px;background:var(--card);padding:28px 30px}
.svc svg{display:block;width:52px;height:52px}
.svc .rule{width:86px;height:2px;background:#9aa3b0;margin:16px 0 14px}
.svc h3{font-family:var(--display);font-weight:400;font-size:14px;line-height:22px;text-transform:uppercase;white-space:nowrap}
.svc.is-active{background:var(--blue);color:var(--white)}
.svc.is-active .rule{background:rgba(255,255,255,.7)}
.svc.more{background:var(--navy);color:var(--white)}

/* edge */
.edge-visual{left:147px;top:2447px;width:489px;height:314px;background:linear-gradient(160deg,#0d2036 0%,#2b5d8a 45%,#d9a35a 75%,#14243a 100%)}
.stripe{position:absolute;transform:skewX(-20deg)}
.edge-title{left:673px;top:2476px;font-size:30px}
.edge-copy{left:673px;top:2535px;width:400px;font-size:12px;line-height:22.5px;color:#222}
.edge-copy p{margin-bottom:22px}

/* expect */
.expect-title{left:125px;top:2905px;font-size:30px;line-height:38px}
.expect-copy{left:125px;top:3046px;width:460px;font-size:9.5px;line-height:18px;color:#333}
.expect-copy p{margin-bottom:18px}
.wheel-visual{left:603px;top:2905px;width:500px;height:500px;background:linear-gradient(135deg,#2496ee 0%,#6fb838 50%,#f7941d 100%)}

/* contact */
.map{left:0;top:3529px;width:590px;height:636px;background:radial-gradient(ellipse at 50% 50%,#e4e7ec 0%,#f1f3f6 60%,#fff 100%)}
.pin{position:absolute}
.contact-card{left:592px;top:3507px;width:484px;height:667px;background:var(--white);box-shadow:0 4px 24px rgba(0,0,0,.12);padding:36px 29px 0}
.contact-card h2{font-size:30px;margin-bottom:20px;white-space:nowrap}
.field{height:37px;background:var(--card);margin-bottom:16px;font-size:10px;padding:12px 12px;color:#333}
.field.tall{height:88px}
.legal{font-size:8.5px;line-height:14px;color:#222;margin-bottom:6px}
.legal.check{padding-left:16px;position:relative;font-weight:500}
.legal.check::before{content:"";position:absolute;left:0;top:3px;width:8px;height:8px;border:1px solid #777}

/* footer */
.footer{left:0;top:4267px;width:1200px;height:483px;background:var(--navy);color:var(--white)}
.footer-mark{left:580px;top:55px;width:40px;height:40px;background:var(--orange)}
.footer-name{position:absolute;left:0;top:150px;width:1200px;text-align:center;font-family:var(--display);font-size:24px;text-transform:uppercase}
.footer-nav a{position:absolute;top:246px;color:var(--white);font-size:12px;text-decoration:none}
.social{position:absolute;top:312px;width:24px;height:24px;border-radius:50%;background:var(--blue)}
.footer-rule{left:125px;top:429px;width:951px;height:1px;background:rgba(255,255,255,.6)}
.footer-small{position:absolute;top:447px;font-size:9px}
</style>
</head>
<body>

<!-- HERO -->
<header class="hero">
  <div class="hero-visual" role="img" aria-label="Satellite orbiting above Earth with glowing network lines"></div>
  <nav class="nav">
    <a style="left:125px">Home</a>
    <a style="left:197px">Advisory Services</a>
    <a style="left:334px">About Us</a>
    <a style="left:862px">Blog</a>
  </nav>
  <div class="brand" style="left:492px;top:36px"><i></i>Harrowgate Lumen Advisors</div>
  <div class="btn" style="left:922px;top:30px;width:153px;height:31px">Contact Now<span class="dot"></span></div>
  <p class="abs welcome">Welcome To <b>HLA</b></p>
  <div class="abs hero-mark"></div>
  <p class="abs hero-copy">Harrowgate Lumen Advisors Connects The Federal Ecosystem With Mission-Critical Technologies—Delivering Communications, Government Affairs, And Marketing Strategies That Drive Growth, Protect Market Share, And Achieve Essential Mission Objectives.</p>
  <h1 class="abs display hero-title">Accelerate<br>Your <span class="outline">Mission</span></h1>
</header>

<!-- INTRODUCTION -->
<section>
  <div class="abs intro-visual" role="img" aria-label="Satellite and network lines inside a hexagonal frame"></div>
  <h2 class="abs display intro-title">Introduction</h2>
  <div class="abs intro-copy">
    <p>Our Team Of Award-Winning Communications Strategists Bring Deep Experience Across Government, Defense, And Technology. We Build Systems, Teams, And Campaigns That Drive Outcomes For Federal Contractors And Innovators Supporting National Security, Space, And Industrial Growth.</p>
    <p>Our Team Has Served In The Military, Supported The DoD And Federal Leaders, And Led Communications, Marketing, And Government Affairs For Major Government, Defense, Tech And Investment Organizations. We Understand The Missions That Matter — And We Help Our Clients Achieve Them Through Precision Communications, Policy Engagement, And Strategic Connection-Building.</p>
    <p>We Are Committed To Strengthening The Defense Industrial Base And Enabling Our Clients To Thrive Through Growth And Transition To Achieve Mission Success.</p>
  </div>
</section>

<!-- PROVEN RESULTS -->
<section>
  <h2 class="abs display results-title">Proven Results<br>That Drive Real<br>Growth</h2>
  <p class="abs results-copy">We've Helped Brands Strengthen Their Digital Presence, Expand Their Network, And Accelerate Opportunities Across The Defense, Space, And Government Sectors. In Just One Year, Our Clients Have Achieved:</p>
  <h3 class="abs display growth-title">Business Growth &amp; Network<br>Expansion</h3>
  <div class="abs stat" style="left:125px;top:1462px">+72%</div>
  <p class="abs stat-note" style="left:125px;top:1508px">Increase In Database Contacts Through CRM Implementation And Targeted Marketing Campaigns</p>
  <div class="abs stat" style="left:343px;top:1462px">100+</div>
  <p class="abs stat-note" style="left:343px;top:1508px">Introductions To Tech-Scouting Contracts Across The DoD And The Aerospace &amp; Defense Ecosystem</p>
  <div class="abs stat" style="left:125px;top:1580px">570%</div>
  <p class="abs stat-note" style="left:125px;top:1626px;width:410px">Positioned A Client For Transformative Growth, Fueling A 570% Increase In Stock Price And Attracting $50M AUD In New Investment</p>
  <div class="abs arrow-btn" style="left:125px"><svg width="14" height="14" viewBox="0 0 14 14"><path d="M9 2 4 7l5 5" fill="none" stroke="#fff" stroke-width="2"/></svg></div>
  <div class="abs arrow-btn" style="left:170px"><svg width="14" height="14" viewBox="0 0 14 14"><path d="M5 2l5 5-5 5" fill="none" stroke="#fff" stroke-width="2"/></svg></div>

  <article class="quote-card faded" style="left:628px;top:1165px;width:463px;height:171px">
    <span class="qmark" style="right:12px;top:0;color:#e3e6eb">&ldquo;</span>
    <div class="who"><div class="avatar"></div><div><div class="name">Dana Whitlock</div><div class="role">President And Managing Director<br>Ironvale Alloys USA</div></div></div>
    <p>Partnering With Harrowgate Lumen Advisors Accelerated The Growth Of Our Company. Their Strategic Insight, Deep Federal Expertise, And Hands-On Support Transformed Our U.S. Expansion. In Less Than Six Months, They Built Our Presence In The United States From The Ground Up, Helping Us Secure Contacts, Advocates, And Visibility At The Highest Levels.</p>
  </article>

  <article class="quote-card active" style="left:593px;top:1369px;width:467px;height:138px;padding-top:12px">
    <span class="qmark" style="right:12px;top:-8px;color:var(--navy)">&ldquo;</span>
    <div class="who" style="margin-bottom:8px"><div class="avatar" style="background:#fff"></div><div><div class="name">Marcus</div><div class="role">Kettering Cole Associates Account Lead</div></div></div>
    <p>Collaborating With Harrowgate Lumen Advisors Was A Game-Changer. Their Innovative Approach And Strategic Insight Propelled Our Work To New Heights. Their Unwavering Commitment To Not Just Meeting, But Exceeding Expectations, Has Been A Cornerstone Of Our Success.</p>
  </article>

  <article class="quote-card faded" style="left:628px;top:1533px;width:463px;height:218px;color:#a9afb8">
    <span class="qmark" style="right:12px;top:-6px;color:var(--navy)">&ldquo;</span>
    <div class="who"><div class="avatar"></div><div style="color:var(--ink)"><div class="name">Elena Brandt</div><div class="role">Vice President Of Customer Success<br>Summit Forge</div></div></div>
    <p>Partnering With Harrowgate Lumen Advisors Was Key To Making Our Flagship Summit A Major Success. We Sold Out Three Weeks Before Our Event, Secured Speakers Who Had Never Worked With Our Organization, And Significantly Expanded Our Network. Their Expertise In Strategic Speaker Acquisition Was Evident Throughout The Entire Process, Identifying Over 300 Top Industry Experts Aligned With Our Event's Themes And Audience.</p>
  </article>
</section>

<!-- SERVICES -->
<section>
  <div class="abs services-band"></div>
  <h2 class="abs display services-title">Our Services</h2>

  <div class="svc" style="left:125px;top:1978px;height:156px">
    <svg viewBox="0 0 52 52" fill="none" stroke="#1c2c44" stroke-width="1.6"><path d="M6 20h40L26 8z"/><path d="M10 22v18M17 22v18M24 22v18M31 22v18M38 22v18M44 22v18"/><path d="M6 42h40M4 46h44"/></svg>
    <div class="rule"></div><h3>Government Affairs</h3>
  </div>
  <div class="svc is-active" style="left:450px;top:1978px;height:156px">
    <svg viewBox="0 0 52 52" fill="none" stroke="#fff" stroke-width="1.8"><circle cx="12" cy="26" r="6"/><circle cx="36" cy="12" r="6"/><circle cx="36" cy="40" r="6"/><path d="M17 23l14-8M17 29l14 8"/></svg>
    <div class="rule"></div><h3>Crisis Communications</h3>
  </div>
  <div class="svc" style="left:772px;top:1978px;height:156px">
    <svg viewBox="0 0 52 52" fill="none" stroke="#1c2c44" stroke-width="1.6"><path d="M6 46h40"/><rect x="9" y="32" width="6" height="14"/><rect x="19" y="26" width="6" height="20"/><rect x="29" y="20" width="6" height="26"/><rect x="39" y="12" width="6" height="34"/><path d="M8 26l12-10 8 6 14-14M36 8h6v6"/></svg>
    <div class="rule"></div><h3>Investor Relations</h3>
  </div>
  <div class="svc" style="left:125px;top:2151px;height:178px">
    <svg viewBox="0 0 52 52" fill="none" stroke="#1c2c44" stroke-width="1.6"><rect x="4" y="8" width="44" height="40"/><path d="M4 18h44M14 4v8M38 4v8"/><path d="M26 23l3 6 6 .8-4.5 4.2 1.1 6L26 37l-5.6 3 1.1-6L17 29.8l6-.8z"/></svg>
    <div class="rule" style="margin-top:24px"></div><h3>Event Management</h3>
  </div>
  <div class="svc" style="left:450px;top:2151px;height:186px">
    <svg viewBox="0 0 52 52" fill="none" stroke="#1c2c44" stroke-width="1.6"><rect x="19" y="4" width="14" height="26" rx="7"/><path d="M13 24a13 13 0 0 0 26 0M26 37v9M18 46h16M19 14h6M19 20h6"/></svg>
    <div class="rule" style="margin-top:24px"></div><h3>Corporate<br>Communications</h3>
  </div>
  <div class="svc more" style="left:772px;top:2151px;height:159px;padding-top:40px">
    <h3 style="font-size:18px">+4 More</h3>
    <div class="btn" style="left:30px;top:83px;width:151px;height:33px">Learn More<span class="dot"></span></div>
  </div>
</section>

<!-- OUR EDGE -->
<section>
  <div class="stripe" style="left:128px;top:2500px;width:12px;height:120px;background:var(--navy)"></div>
  <div class="stripe" style="left:120px;top:2560px;width:16px;height:120px;background:var(--blue)"></div>
  <div class="stripe" style="left:175px;top:2700px;width:10px;height:100px;background:var(--navy)"></div>
  <div class="abs edge-visual" role="img" aria-label="Astronauts looking out a station window at Earth"></div>
  <h2 class="abs display edge-title">Our Edge</h2>
  <div class="abs edge-copy">
    <p>We Combine Deep Federal Sector Insight, Technical Understanding, And A Powerful Network Across Government, Industry, Investors, And Media. Our Proven Approach Drives Results — From Major Contract Wins And Successful M&amp;A To Increased Valuation, Strategic Investment, And Political Support.</p>
    <p>Our Strategies Begin With Your Mission And Business Goals, Ensuring Every Message, Relationship, And Action Advances Growth And Impact.</p>
  </div>
</section>

<!-- WHAT TO EXPECT -->
<section>
  <h2 class="abs display expect-title">What To Expect<br>When Partnering<br>With Us</h2>
  <div class="abs expect-copy">
    <p>With Decades Of Experience, A Results-Focused Methodology, And Cutting-Edge Marketing And Communications Tools And Technologies, We Begin Every Engagement With A Discovery And Planning Process To Ensure We Are Building A Strategy That Cuts Through The Noise To Achieve Our Measurable Results.<br>As Specialists In Government Crisis Communications, We Additionally Examine Our Client's Current Strategy For Risks Ensuring We Are Building On A Stable Foundation.</p>
    <p>By Truly Understanding Our Client's Goals, Key Milestones, Potential Areas Of Risk, Ideal Customer And Investor Targets, Partner Profiles, And Other Key Drivers, We Create Messaging And Strategy That Goes Beyond Traditional Brand Awareness To Meet Mission Objectives. As A Full Service Firm, We Work Across All The Areas In The Graphic.</p>
    <p>Our Time-Tested Methodology Is Based On Building And Executing A Strategy Aligned With Client Mission Objectives. With The Strategy In Place, We Execute Tactics With Precision, Efficiency, And The Highest Quality Of Service.</p>
  </div>
  <div class="btn" style="left:125px;top:3360px;width:151px;height:31px">Get In Touch<span class="dot"></span></div>
  <div class="abs wheel-visual" role="img" aria-label="Circular brand services infographic covering messaging, government affairs, marketing and brand development"></div>
</section>

<!-- CONTACT -->
<section>
  <div class="abs map" role="img" aria-label="Dotted world map showing office locations"></div>
  <svg class="pin" style="left:155px;top:3690px" width="30" height="40" viewBox="0 0 30 40"><path d="M15 0C7 0 1 6 1 14c0 10 14 26 14 26s14-16 14-26C29 6 23 0 15 0z" fill="#0f2c52"/><circle cx="15" cy="14" r="6" fill="#fff"/></svg>
  <svg class="pin" style="left:488px;top:3696px" width="22" height="30" viewBox="0 0 30 40"><path d="M15 0C7 0 1 6 1 14c0 10 14 26 14 26s14-16 14-26C29 6 23 0 15 0z" fill="#0f2c52"/><circle cx="15" cy="14" r="6" fill="#fff"/></svg>
  <svg class="pin" style="left:262px;top:3960px" width="22" height="30" viewBox="0 0 30 40"><path d="M15 0C7 0 1 6 1 14c0 10 14 26 14 26s14-16 14-26C29 6 23 0 15 0z" fill="#0f2c52"/><circle cx="15" cy="14" r="6" fill="#fff"/></svg>

  <form class="abs contact-card">
    <h2 class="display">Contact Us Now</h2>
    <div class="field">Email</div>
    <div class="field">Company Name</div>
    <div class="field">Full Name</div>
    <div class="field">Website URL</div>
    <div class="field">Phone Number</div>
    <div class="field tall">Tell Us More How We Help You</div>
    <p class="legal">We hate spam as much as you do! However we need your permission to reach out from time to time and save your email address.</p>
    <p class="legal check">I agree to receive communications from Harrowgate Lumen Advisors</p>
    <p class="legal">You can unsubscribe from these communications at any time. Please review our Privacy Policy for more details.</p>
    <p class="legal">By clicking submit below, you consent to allow Harrowgate Lumen Advisors to store and process the personal information submitted above to provide you the content requested.</p>
    <div class="btn" style="left:29px;top:607px;width:426px;height:33px">Submit Now<span class="dot"></span></div>
  </form>
</section>

<!-- FOOTER -->
<footer class="abs footer">
  <div class="abs footer-mark"></div>
  <div class="footer-name">Harrowgate Lumen Advisors</div>
  <nav class="footer-nav">
    <a style="left:348px">Home</a>
    <a style="left:407px">Advisory</a>
    <a style="left:482px">Services</a>
    <a style="left:555px">About Us</a>
    <a style="left:632px">Blog</a>
  </nav>
  <div class="btn" style="left:699px;top:237px;width:152px;height:33px">Contact Now<span class="dot"></span></div>
  <span class="social" style="left:535px"></span>
  <span class="social" style="left:570px"></span>
  <span class="social" style="left:605px"></span>
  <span class="social" style="left:640px"></span>
  <div class="abs footer-rule"></div>
  <span class="footer-small" style="left:125px">Copyright © 2025 All Right Reserved</span>
  <span class="footer-small" style="left:812px">Privacy Policy</span>
  <span class="footer-small" style="left:900px">Terms Of Service</span>
  <span class="footer-small" style="left:1000px">Cookies Settings</span>
</footer>

</body>
</html>
```